Rug Cleaning Web Design Project

We need a web design for our cleaning company. We currently have a web page but are not happy with its design. We currently offer fine rug cleaning,upholstery cleaning, and residential and commercial carpet cleanning. We also offer water damage restoration. For our rug cleaning services we offer : Enzyme treatments for pet contamination and odor removal, application of stain protection that is designed for the fine textiles used in rug construction, application of treatments designed to prevent moth damage and pads designed to be used under rugs.Our current web site is harborfreshcare.example. We are intrested in a design with similar information to the web page of Velmora Rug Cleaners INC. We would like to use the colors that are present in our logo that will be uploaded with this description. We would also like this new page to be linked to our other address loomrinsepro.example. We would like the deign to be visually attractive but not "too busy".
Updates

Please include pictures of rugs, or people washing rugs if possible. We do not offer maid type cleaning services. We would not be interested in designs including pictures depicting that type service. Thanks for your hard work on this project.

Dana Whitlow

Industry/Entity Type

Residential

Requirements
Must have
• This page must be viewable on smart phones and tablets.

```html
<!DOCTYPE html>
<html lang="en">
<head>
<meta charset="utf-8">
<meta name="viewport" content="width=device-width, initial-scale=1">
<title>Rug Cleaning</title>
<link rel="stylesheet" href="https://fonts.googleapis.com/css2?family=Source+Sans+3:wght@300;400&family=Arimo:wght@400;700&display=swap">
<style>
  :root {
    --page-bg: #f1f2f2;
    --header-bg: #f6f6f6;
    --logo-dark: #2f4c66;
    --logo-light: #5e8aa8;
    --heading: #3d5a72;
    --banner-top: #55788f;
    --banner-mid: #9cb3c2;
    --banner-low: #dce3e8;
    --stripe: #3f6f8c;
    --text: #1c1c1c;
    --muted: #333;
    --rule: #d6d9db;
    --white: #ffffff;
    --social: #3b8fd0;
  }
  * { box-sizing: border-box; margin: 0; padding: 0; }
  html, body { width: 1200px; height: 871px; overflow: hidden; }
  body { background: var(--page-bg); font-family: "Arimo", Arial, sans-serif; color: var(--text); position: relative; }

  .site-header { position: absolute; left: 0; top: 0; width: 1200px; height: 87px; background: var(--header-bg); border-bottom: 4px solid #e2e4e5; }
  .brand { position: absolute; left: 190px; top: 22px; font-family: "Source Sans 3", sans-serif; font-weight: 400; font-size: 38px; letter-spacing: 0.5px; color: var(--logo-dark); line-height: 1; }
  .social { position: absolute; left: 914px; top: 35px; display: flex; gap: 9px; }
  .social span { width: 21px; height: 21px; border-radius: 3px; background: var(--social); display: block; }

  .banner { position: absolute; left: 0; top: 91px; width: 1200px; height: 296px;
    background: linear-gradient(180deg, var(--banner-top) 0%, #7f9db0 35%, var(--banner-mid) 65%, var(--banner-low) 94%, #eef1f3 100%); }
  .banner-stripe { position: absolute; left: 0; top: 373px; width: 1200px; height: 14px;
    background: linear-gradient(180deg, var(--stripe) 0 4px, #9fb8c8 4px 7px, #2e5f7c 7px 11px, #c9d6de 11px 14px); }
  .banner-fade { position: absolute; left: 0; top: 387px; width: 1200px; height: 60px; background: linear-gradient(180deg, #c9d3d9, var(--page-bg)); }

  .main-nav { position: absolute; left: 171px; top: 114px; display: flex; align-items: center; font-family: "Source Sans 3", sans-serif; font-size: 16.5px; color: var(--white); }
  .main-nav a { color: inherit; text-decoration: none; margin-right: 27px; }
  .main-nav a.active { background: var(--white); color: var(--heading); border-radius: 4px; width: 85px; height: 35px; line-height: 35px; text-align: center; margin-right: 25px; box-shadow: 0 1px 2px rgba(0,0,0,.25); }
  .main-nav a:nth-child(3) { margin-right: 43px; }
  .main-nav a:nth-child(4) { margin-right: 44px; }

  .hero-kicker { position: absolute; left: 190px; top: 191px; font-family: "Source Sans 3", sans-serif; font-size: 25px; color: var(--heading); letter-spacing: -0.5px; }
  .hero-title { position: absolute; left: 190px; top: 213px; font-family: "Source Sans 3", sans-serif; font-weight: 400; font-size: 37px; color: var(--white); letter-spacing: -0.7px; text-shadow: 0 1px 2px rgba(0,0,0,.3); }
  .hero-text { position: absolute; left: 190px; top: 272px; width: 490px; font-size: 12.7px; line-height: 19px; color: var(--text); }

  .hero-product { position: absolute; left: 693px; top: 80px; width: 345px; height: 396px; border-radius: 40px 40px 20px 20px;
    background: radial-gradient(ellipse at 45% 70%, #2a2d31 0%, #1a1c1f 45%, rgba(30,35,40,0.15) 75%, rgba(0,0,0,0) 100%); }

  .welcome-title { position: absolute; left: 190px; top: 426px; font-family: "Source Sans 3", sans-serif; font-weight: 300; font-size: 28px; color: var(--heading); letter-spacing: -0.6px; }
  .intro { position: absolute; left: 190px; top: 477px; width: 482px; font-weight: 700; font-size: 12.7px; line-height: 18.9px; color: var(--text); }
  .intro-photo { float: left; width: 175px; height: 175px; margin: 0 23px 4px 0; border: 1px solid #cfcfcf;
    background: linear-gradient(180deg, #f4f4f4 0%, #e7e7e7 55%, #3a3a3a 80%, #d9d4c8 100%); }

  .column-rule { position: absolute; left: 702px; top: 473px; width: 1px; height: 398px; background: var(--rule); }

  .section-title { position: absolute; left: 733px; font-family: "Source Sans 3", sans-serif; font-weight: 300; font-size: 28px; color: var(--heading); letter-spacing: -0.6px; }
  .work-grid { position: absolute; left: 733px; top: 525px; display: grid; grid-template-columns: repeat(3, 83px); gap: 9px 9px; }
  .work-grid span { width: 83px; height: 83px; border: 1px solid #c9c9c9; display: block; }
  .w1 { background: linear-gradient(160deg, #cfc9c2, #8f8680); }
  .w2 { background: linear-gradient(160deg, #e6e2dc, #c0473c 60%, #d8d2c4); }
  .w3 { background: linear-gradient(160deg, #e7e3d8, #b9a48a); }
  .w4 { background: linear-gradient(160deg, #f2f2f2, #d8cfc2); }
  .w5 { background: linear-gradient(180deg, #c3bfb8, #e9e5de); }
  .w6 { background: linear-gradient(180deg, #e8ebe5, #c8d2bf); }

  .news-date { position: absolute; left: 733px; top: 782px; font-weight: 700; font-size: 12.2px; }
  .news-text { position: absolute; left: 733px; top: 803px; width: 270px; font-size: 12.2px; line-height: 19px; color: var(--muted); }
  .news-rule { position: absolute; left: 733px; top: 853px; width: 266px; border-top: 1px dotted #b8b8b8; }

  .services-title { position: absolute; left: 190px; top: 834px; font-family: "Source Sans 3", sans-serif; font-weight: 300; font-size: 28px; color: var(--heading); letter-spacing: -0.6px; }
</style>
</head>
<body>
  <header class="site-header">
    <div class="brand">RUG CLEANING</div>
    <div class="social" aria-label="Social links"><span></span><span></span><span></span></div>
  </header>

  <div class="banner"></div>
  <div class="banner-stripe"></div>
  <div class="banner-fade"></div>

  <nav class="main-nav">
    <a class="active" href="#">HOME</a>
    <a href="#">ABOUT</a>
    <a href="#">SERVICES</a>
    <a href="#">TESTIMONIALS</a>
    <a href="#">CONTACTS</a>
  </nav>

  <div class="hero-kicker">We Will Make</div>
  <h1 class="hero-title">Your Carpets Clean and Fresh</h1>
  <p class="hero-text">We need a web design for our cleaning company. We currently have a web page but are not happy with its design. We currently offer fine rug cleaning,upholstery cleaning, and residential and commercial carpet cleanning.</p>

  <div class="hero-product" role="img" aria-label="Black canister vacuum cleaner with hose and floor nozzle"></div>

  <h2 class="welcome-title">Welcome to Rug Carpet Cleaning!</h2>
  <div class="intro">
    <div class="intro-photo" role="img" aria-label="Woman vacuuming a shaggy rug in a bright room"></div>
    We need a web design for our cleaning company. We currently have a web page but are not happy with its design. We currently offer fine rug cleaning,upholstery cleaning, and residential and commercial carpet cleanning. We also offer water damage restoration. For our rug cleaning services we offer : Enzyme treatments for pet contamination and odor removal, application of stain protection that is designed for the fine textiles used in rug construction, application of treatments designed to prevent moth damage and pads designed to be used under rugs.Our current web site is harborfreshcare.example. We are intrested in a design with similar information to the web page of Velmora Rug Cleaners INC. We would like to use the colors that are present in our logo that will be uploaded with this description. We would also like this new page to be linked to our other address loomrinsepro.example. We would like the deign to be visually attractive but not "too busy".
  </div>

  <div class="column-rule"></div>

  <h2 class="section-title" style="top:473px">Our Work</h2>
  <div class="work-grid">
    <span class="w1" role="img" aria-label="Man vacuuming a carpet"></span>
    <span class="w2" role="img" aria-label="Hand scrubbing a floor with a sponge"></span>
    <span class="w3" role="img" aria-label="Woman cleaning a carpet by hand"></span>
    <span class="w4" role="img" aria-label="Vacuum hose on a light carpet"></span>
    <span class="w5" role="img" aria-label="Carpeted staircase with a basket"></span>
    <span class="w6" role="img" aria-label="Man vacuuming a living room floor"></span>
  </div>

  <h2 class="section-title" style="top:726px">Recent News</h2>
  <div class="news-date">10.19.2012</div>
  <p class="news-text">This will be a flash news. Here your news will scroll up or down</p>
  <div class="news-rule"></div>

  <h2 class="services-title">Our Services</h2>
</body>
</html>
```